Our winery needs a company flyer

We need a flyer describing our family winery and our excellent wines. We would like to be attractive fresh and young for people from 30 to 50 years old. the vineyards are planted from the family and our wines are a selected production. We love nature !
The final design should communicate "a good job produce a good wine". look at our website www.belsaritavini.ch

It Company

```html
<!DOCTYPE html>
<html lang="it">
<head>
<meta charset="utf-8">
<title>Belsarita – Flyer</title>
<link href="https://fonts.googleapis.com/css2?family=Questrial&display=swap" rel="stylesheet">
<style>
:root{
  --stage:#333333;
  --ink:#111111;
  --black:#000000;
  --white:#ffffff;
  --teal:#2fb595;
  --teal-text:#3cc9a6;
  --body:#222222;
  --muted:#dddddd;
}
*{margin:0;padding:0;box-sizing:border-box}
html,body{width:1200px;height:900px;overflow:hidden}
body{background:var(--stage);font-family:"Questrial",sans-serif;position:relative}
.page{position:absolute;top:130px;width:459px;height:648px;background:var(--white);overflow:hidden}
.page--front{left:117px}
.page--back{left:639px}
.abs{position:absolute}
.photo{position:absolute}

/* front */
.masthead{left:0;top:0;width:459px;height:96px;background:var(--black);color:var(--white);text-align:center}
.brand{font-size:46px;letter-spacing:3px;line-height:1;padding-top:10px}
.tagline{font-size:17px;letter-spacing:.5px;margin-top:14px}
.hero{left:0;top:96px;width:459px;height:291px;
  background:linear-gradient(120deg,#4b4e57 0%,#8a8a8c 35%,#3a3b3f 55%,#6a5a3a 80%,#c9c1a5 100%)}
.label{position:absolute;background:var(--teal);color:var(--white);font-size:11px;letter-spacing:.5px;padding:2px 0 0 6px;height:17px}
.intro{left:23px;top:424px;width:415px;font-size:7.6px;line-height:1.42;color:var(--body)}
.intro p{margin-bottom:1px}
.strip{top:522px;height:108px}
.contact-bar{left:0;top:630px;width:459px;height:18px;background:var(--black);color:var(--white);font-size:9.5px;display:flex;align-items:center;justify-content:space-between;padding:0 15px}
.contact{display:flex;align-items:center;gap:5px}
.contact svg{width:10px;height:10px}

/* back */
.bottles{left:0;top:0;width:246px;height:200px;background:radial-gradient(ellipse at 50% 45%,#d9d9d7 0%,#a9a9a7 55%,#7e7e7c 100%)}
.about{left:258px;top:51px;width:191px;font-size:7.5px;line-height:1.4;color:var(--body);text-align:justify}
.about p{margin-bottom:3px}
.wines{left:0;top:200px;width:459px;height:335px;background:var(--black)}
.wines-title{left:17px;top:32px;width:157px;height:44px;background:var(--teal);color:var(--white);font-size:19px;letter-spacing:1px;display:flex;align-items:center;padding-left:9px}
.thumb{position:absolute;width:60px;height:58px;border-radius:4px;background:linear-gradient(135deg,#f2f0ea,#c9c5b8)}
.wine{position:absolute;color:var(--muted);font-size:6.4px;line-height:1.42}
.wine h3{color:var(--teal-text);font-weight:400;font-size:10px;letter-spacing:.5px;margin-bottom:5px}
.bottom-photo{top:535px;height:113px}
.web-band{left:139px;top:630px;width:182px;height:18px;background:var(--teal);color:var(--white);font-size:11px;text-align:center;line-height:19px;border-radius:9px 9px 0 0}
</style>
</head>
<body>

<section class="page page--front">
  <header class="abs masthead">
    <div class="brand">BELSARITA</div>
    <div class="tagline">A GOOD JOB PRODUCE A GOOD WINE</div>
  </header>
  <div class="photo hero" role="img" aria-label="Winemaker walking beside netted vineyard rows on a terraced slope in winter sun"></div>

  <div class="label" style="left:23px;top:399px;width:100px">CHI SIAMO</div>
  <div class="abs intro">
    <p>Siamo Lucia e Marco e l'amore per la natura, la vita, la libertà, i viaggi ci ha guidati verso un mondo fatto di idee, atmosfere, sensorialità, piacevolezza.</p>
    <p>Crediamo che per ottenere la serenità che meritiamo dovremmo tutti seguire un modello di vita legato ai tempi che la natura ci indica e che nel nostro caso, le viti che accudiamo, ci insegnano a poco a poco a seguire.</p>
    <p>Crediamo che con il nostro lavoro e attraverso i nostri prodotti possiamo trasmettere le emozioni che ci accompagnano.</p>
    <p>I vini che produciamo sono frutto del nostro impegno a lavorare in sintonia con la natura, del rispetto delle tradizioni e del coraggio dell'innovazione.</p>
  </div>

  <div class="photo strip" style="left:0;width:139px;background:linear-gradient(160deg,#7a8c4a,#b08a5a 55%,#3f6a3a)" role="img" aria-label="Young harvester in straw hat with a crate of grapes"></div>
  <div class="photo strip" style="left:139px;width:182px;background:linear-gradient(150deg,#5a8a3a,#a0b86a 50%,#3a5a2a)" role="img" aria-label="Smiling woman picking grapes among green vines"></div>
  <div class="photo strip" style="left:321px;width:138px;background:linear-gradient(170deg,#9cc06a,#5a7a3a 60%,#2f4a25)" role="img" aria-label="The couple standing together in the vineyard"></div>

  <footer class="abs contact-bar">
    <span class="contact"><svg viewBox="0 0 10 10"><path d="M2 1l2 2-1 1.2c.6 1.2 1.6 2.2 2.8 2.8L7 6l2 2-1.2 1.2C4.5 9 1 5.5.8 2.2z" fill="#fff"/></svg>41 91 5550140</span>
    <span class="contact"><svg viewBox="0 0 10 10"><rect x=".5" y="2" width="9" height="6" fill="none" stroke="#fff"/><path d="M.5 2l4.5 3.5L9.5 2" fill="none" stroke="#fff"/></svg>info@belsaritavini.ch</span>
    <span class="contact"><svg viewBox="0 0 10 10" fill="none" stroke="#fff" stroke-width=".8"><circle cx="5" cy="5" r="4.3"/><ellipse cx="5" cy="5" rx="1.8" ry="4.3"/><path d="M.7 5h8.6M1.5 3h7M1.5 7h7"/></svg>www.belsaritavini.ch</span>
  </footer>
</section>

<section class="page page--back">
  <div class="photo bottles" role="img" aria-label="Four bottles of red wine from the range on a grey backdrop"></div>
  <div class="label" style="left:258px;top:20px;width:95px">CHI SIAMO</div>
  <div class="abs about">
    <p>We Lucia and Marco and the love of nature, life, freedom, travel guided us towards a world of ideas, atmospheres, sensory, pleasantness.</p>
    <p>We believe that to achieve the peace we deserve we should all follow a pattern of life tied to the times that nature shows us and in our case, the screws that accudiamo, we learn gradually to follow.</p>
    <p>We believe that through our work and through our products we can convey the emotions that accompany us.</p>
    <p>The wines we produce are the result of our commitment to work in harmony with nature, respect for tradition and the courage of innovation.</p>
  </div>

  <div class="abs wines">
    <div class="abs wines-title">I NOSTRI VINI</div>

    <div class="thumb" style="left:14px;top:105px" role="img" aria-label="Label of the Aurora wine"></div>
    <div class="wine" style="left:82px;top:109px;width:150px">
      <h3>AURORA</h3>
      color porpora intenso con riflessi rubino. Aroma ampio, giovanile,fruttato (bacche nere e rosse), minerale e delicatamente speziato.<br>Equilibrato al palato con una gradevole presenza di tannini.Persistenza buona con retrogusto fresco, succulento.
    </div>

    <div class="thumb" style="left:14px;top:197px" role="img" aria-label="Label of the Fenice wine"></div>
    <div class="wine" style="left:82px;top:201px;width:150px">
      <h3>FENICE</h3>
      merlot, il blend si completa con altri vitigni<br>Descrizione: Fenice è ottenuto da uve raccolte in vigne con oltre 40 anni di età.<br>La meticolosa e spasmodica cura che dedichiamo ai vigneti, la severa potatura invernale e lo sfoltimento dei grappoli in eccesso per regolare la bassa produzione consentono la raccolta di un prodotto di estrema qualità e di forte concentrazione.
    </div>

    <div class="thumb" style="left:243px;top:12px" role="img" aria-label="Label of the Belsarita wine"></div>
    <div class="wine" style="left:312px;top:14px;width:138px">
      <h3>BELSARITA</h3>
      E' un vino morbido e armonioso con bei tannini equilibrati e dolci grazie all'affinamento in botti nuove di rovere francese per 17 mesi.<br>Questo Merlot ha color rubino intenso e concentrato, una salda tessitura di profumi caldi, con note prevalenti di marmellata di more, e sottobosco che emergono in un quadro aromatico pronunciato.
    </div>

    <div class="thumb" style="left:243px;top:113px" role="img" aria-label="Label of the Marmora wine"></div>
    <div class="wine" style="left:312px;top:115px;width:138px">
      <h3>MARMORA</h3>
      Di colore rosso rubino intenso con riflessi violacei. Un vino che riposa in parte per 12 mesi in nuove barrique spagnole della regione del Rioja. Pertanto dotato di notevole carattere.<br>Un vino fruttato dal quale emergono una nota di composta di frutta, una nota di vaniglia dolce ed elegante tipica delle barriques spagnole, una delicata nota balsamica e un sentore di spezie.Equilibrato e ricco al palato.
    </div>

    <div class="thumb" style="left:243px;top:235px" role="img" aria-label="Label of the Zenobia wine"></div>
    <div class="wine" style="left:312px;top:237px;width:138px">
      <h3>ZENOBIA</h3>
      colore brillante, giallo dorato con leggeri riflessi ambrati. Aroma pronunciato e complesso. Profumo di frutta esotica matura, floreale ed erbaceo, con un'elegante nota agrumata. Corpo importante e pieno. Sapore vinoso, con sentori di piccola frutta gialla. Retrogusto secco, piacevolmente amaro e dalla fresca acidità.
    </div>
  </div>

  <div class="photo bottom-photo" style="left:0;width:139px;background:linear-gradient(180deg,#3a3d40,#8a8e92 50%,#2a2c2e)" role="img" aria-label="Stainless steel fermentation tanks in the cellar"></div>
  <div class="photo bottom-photo" style="left:139px;width:182px;background:linear-gradient(180deg,#cfe3f0 0%,#a9c9e0 40%,#6f8f5a 62%,#4a6a35 100%)" role="img" aria-label="Vineyard valley with mountains under a bright sky"></div>
  <div class="photo bottom-photo" style="left:321px;width:138px;background:linear-gradient(150deg,#3a2518,#a06a3a 50%,#5a3a22)" role="img" aria-label="Oak barrels stacked in the cellar"></div>
  <div class="abs web-band">www.belsaritavini.ch</div>
</section>

</body>
</html>
```